Ledgerwise Systems Group business card design.

We are a software development company that develop Software for finance companies and related industries.

We need a 2 sided business card designed. We have a new logo already designed (see attached eps and ai) We are after a clean simple corporate look. One side with just our logo, and the second side with our details.

Mark Hollister
Managing Director

Suite 4 Level 9, 138 Kellaway Street Sydney NSW 2000

Direct: +61 2 9374 6021
Mobile: +61 4 2287 5196
Email: markh@lsg-example.net.au
Web: www.lsg-example.net.au

I have included 2 logo files an .ai and .eps. I noticed that the lines either side of the group looks a bit jaggered and needs to be made sharper.

I would like to introduce a little colour somewhere rather than having it all black and white. But not over the top, keeping with a simple clean corporate look. Perhaps a light blue on some of the text?

If you have other ideas would be pleased to review

Regards

Mark H.

```html
<!DOCTYPE html>
<html lang="en">
<head>
<meta charset="utf-8">
<title>Ledgerwise Systems Group — Business Card</title>
<link rel="stylesheet" href="https://fonts.googleapis.com/css2?family=Open+Sans:wght@400;600;700&display=swap">
<style>
  :root {
    --page-bg: #e9e7e4;
    --card-black: #0b0b0c;
    --card-sheen: #1e1f22;
    --ink-white: #ffffff;
    --ink-soft: #d9dadc;
    --accent-blue: #6cb4e4;
    --rule-grey: #8a8c90;
  }
  * { box-sizing: border-box; margin: 0; padding: 0; }
  html, body {
    width: 1200px;
    height: 913px;
    overflow: hidden;
    background: var(--page-bg);
    font-family: "Open Sans", Arial, sans-serif;
  }
  .stage {
    position: relative;
    width: 1200px;
    height: 913px;
  }
  .card {
    position: absolute;
    width: 540px;
    height: 330px;
    border-radius: 6px;
    background: linear-gradient(135deg, var(--card-sheen) 0%, var(--card-black) 55%, #000 100%);
    box-shadow: 0 14px 30px rgba(0,0,0,0.28);
    overflow: hidden;
  }
  .card--front { left: 70px; top: 110px; }
  .card--back  { left: 590px; top: 470px; }

  /* Front side */
  .front-decor {
    position: absolute;
    right: -40px;
    top: -60px;
    width: 300px;
    height: 300px;
    background: rgba(255,255,255,0.035);
    transform: rotate(12deg);
  }
  .brand {
    position: absolute;
    left: 0; right: 0;
    top: 50%;
    transform: translateY(-50%);
    display: flex;
    flex-direction: column;
    align-items: center;
    gap: 18px;
  }
  .brand__mark {
    width: 64px;
    height: 64px;
    background: var(--ink-white);
  }
  .brand__name {
    color: var(--ink-white);
    font-weight: 700;
    font-size: 27px;
    letter-spacing: 1.5px;
    text-transform: uppercase;
    text-align: center;
    line-height: 1.15;
  }

  /* Back side */
  .back-brand {
    position: absolute;
    left: 34px;
    top: 118px;
    width: 230px;
    display: flex;
    flex-direction: column;
    align-items: flex-start;
    gap: 14px;
  }
  .back-brand__mark {
    width: 92px;
    height: 92px;
    background: var(--ink-white);
  }
  .back-brand__name {
    color: var(--ink-white);
    font-weight: 700;
    font-size: 19px;
    letter-spacing: 1px;
    text-transform: uppercase;
    line-height: 1.2;
  }
  .details {
    position: absolute;
    left: 300px;
    top: 52px;
    width: 220px;
    color: var(--ink-soft);
    font-size: 11.5px;
    line-height: 1.45;
  }
  .details__name {
    color: var(--accent-blue);
    font-weight: 700;
    font-size: 15px;
  }
  .details__role {
    color: var(--ink-soft);
    font-size: 11px;
    margin-bottom: 22px;
  }
  .details__address { margin-bottom: 14px; }
  .contact-list { list-style: none; }
  .contact-list li {
    display: flex;
    align-items: center;
    gap: 8px;
    white-space: nowrap;
  }
  .contact-list svg {
    width: 11px;
    height: 11px;
    flex: none;
    fill: var(--accent-blue);
  }
</style>
</head>
<body>
<main class="stage">

  <section class="card card--front" aria-label="Card front">
    <div class="front-decor"></div>
    <div class="brand">
      <div class="brand__mark"></div>
      <div class="brand__name">Ledgerwise Systems Group</div>
    </div>
  </section>

  <section class="card card--back" aria-label="Card back">
    <div class="back-brand">
      <div class="back-brand__mark"></div>
      <div class="back-brand__name">Ledgerwise<br>Systems Group</div>
    </div>

    <div class="details">
      <div class="details__name">Mark Hollister</div>
      <div class="details__role">Managing Director</div>
      <p class="details__address">Suite 4 Level 9, 138 Kellaway Street<br>Sydney NSW 2000</p>
      <ul class="contact-list">
        <li>
          <svg viewBox="0 0 12 12" aria-hidden="true"><path d="M1 4c0-1 1-2 2-2h6c1 0 2 1 2 2v1H8V4H4v1H1z M2 6h8l1 5H1z"/></svg>
          +61 2 9374 6021
        </li>
        <li>
          <svg viewBox="0 0 12 12" aria-hidden="true"><path d="M3 0h6v12H3z M4 1.5v8h4v-8z"/></svg>
          +61 4 2287 5196
        </li>
        <li>
          <svg viewBox="0 0 12 12" aria-hidden="true"><path d="M0 2h12v8H0z M1 3l5 4 5-4v-.2H1z" fill-rule="evenodd"/></svg>
          markh@lsg-example.net.au
        </li>
        <li>
          <svg viewBox="0 0 12 12" aria-hidden="true"><circle cx="6" cy="6" r="5.5"/></svg>
          www.lsg-example.net.au
        </li>
      </ul>
    </div>
  </section>

</main>
</body>
</html>
```